Aged Care Consultancy Business needs a business card design

I need a two sided business card - I want it clean and professional. Surprise me

Target Market(s)

middle aged and ageing victorians

Industry/Entity Type

Health Care

Contact Information for Business Card

Text to be included

Logo
Aged Care Consulting Services
Professional, Reliable, Affordable

Tovan Brelsick
Director
0427 31 64 92 (larger)
1300 73 29 41
tovan@wadolire.com.au
www.wadolcare.com.au
Friendlink (details TBA)

include little icons beside the contact info:

- Envelope = email
- Phone = phone
- Globe = website

Font styles to use
Serif
Sans Serif

Requirements
Must have
• look proffesional and clean

```html
<!DOCTYPE html>
<html lang="en">
<head>
<meta charset="UTF-8">
<title>wadol care — business card</title>
<link rel="stylesheet" href="https://fonts.googleapis.com/css2?family=Source+Sans+3:wght@400;600;700&display=swap">
<style>
  :root {
    --backdrop: #e8e3da;
    --card-light: #f2f2f1;
    --card-dark: #1f1f1f;
    --navy: #2b4a80;
    --orange: #e0902e;
    --ink: #262626;
    --logo-light: #7f98c7;
  }
  * { margin: 0; padding: 0; box-sizing: border-box; }
  html, body {
    width: 1200px; height: 443px; overflow: hidden;
    background: var(--backdrop);
    font-family: "Source Sans 3", "Myriad Pro", Arial, sans-serif;
  }
  .canvas { position: relative; width: 1200px; height: 443px; }
  .card {
    position: absolute; top: 86px;
    width: 479px; height: 273px;
    border-radius: 14px;
  }
  .card--front { left: 99px; background: var(--card-light); }
  .card--back { left: 624px; background: var(--card-dark); }

  .identity { position: absolute; left: 25px; top: 24px; padding-left: 14px; }
  .identity__bar {
    position: absolute; left: 0; top: 0;
    width: 6px; height: 40px; background: var(--orange);
  }
  .identity__name { color: var(--navy); font-size: 19px; font-weight: 400; line-height: 22px; }
  .identity__role { color: var(--orange); font-size: 11.5px; line-height: 14px; margin-top: 2px; }

  .brand {
    position: absolute; right: 20px; top: 62px;
    display: flex; align-items: center; gap: 7px;
  }
  .brand__dot { width: 12px; height: 12px; border-radius: 50%; background: var(--orange); }
  .brand__name { color: var(--navy); font-size: 22px; font-weight: 700; line-height: 1; }

  .contacts { position: absolute; left: 28px; top: 145px; list-style: none; }
  .contacts__item {
    display: flex; align-items: center;
    height: 21px; color: var(--ink); font-size: 11.5px;
  }
  .contacts__item--primary { height: 24px; font-size: 15.5px; }
  .contacts__icon { width: 13px; height: 13px; margin-right: 6px; flex: none; }

  .back-brand {
    position: absolute; left: 0; right: 0; top: 0; bottom: 0;
    display: flex; align-items: center; justify-content: center; gap: 12px;
  }
  .back-brand__dot { width: 20px; height: 20px; border-radius: 50%; background: var(--orange); }
  .back-brand__name { color: var(--logo-light); font-size: 40px; font-weight: 600; line-height: 1; }
</style>
</head>
<body>
<div class="canvas">
  <section class="card card--front">
    <div class="identity">
      <span class="identity__bar"></span>
      <p class="identity__name">Tovan Brelsick</p>
      <p class="identity__role">Director</p>
    </div>

    <div class="brand">
      <span class="brand__dot"></span>
      <span class="brand__name">wadol care</span>
    </div>

    <ul class="contacts">
      <li class="contacts__item contacts__item--primary">
        <svg class="contacts__icon" viewBox="0 0 16 16" aria-hidden="true">
          <path fill="var(--orange)" d="M1 5c0-2 3-3 7-3s7 1 7 3v1h-4V5H5v1H1z"/>
          <path fill="var(--orange)" d="M3 8l2-2h6l2 2v6H3z"/>
          <circle cx="8" cy="10.5" r="1.6" fill="var(--card-light)"/>
        </svg>
        0427 31 64 92
      </li>
      <li class="contacts__item">
        <svg class="contacts__icon" viewBox="0 0 16 16" aria-hidden="true">
          <rect x="4.5" y="1" width="7" height="14" rx="1.2" fill="var(--orange)"/>
          <rect x="5.8" y="3" width="4.4" height="8.5" fill="var(--card-light)"/>
        </svg>
        1300 73 29 41
      </li>
      <li class="contacts__item">
        <svg class="contacts__icon" viewBox="0 0 16 16" aria-hidden="true">
          <rect x="1" y="3.5" width="14" height="9" fill="var(--orange)"/>
          <path d="M1 3.5l7 5 7-5" fill="none" stroke="var(--card-light)" stroke-width="1.2"/>
        </svg>
        tovan@wadolire.com.au
      </li>
      <li class="contacts__item">
        <svg class="contacts__icon" viewBox="0 0 16 16" aria-hidden="true">
          <g fill="none" stroke="#9a9a9a" stroke-width="1.1">
            <circle cx="8" cy="8" r="6.3"/>
            <ellipse cx="8" cy="8" rx="2.8" ry="6.3"/>
            <path d="M1.7 8h12.6M2.8 5h10.4M2.8 11h10.4"/>
          </g>
        </svg>
        www.wadolcare.com.au
      </li>
      <li class="contacts__item">
        <svg class="contacts__icon" viewBox="0 0 16 16" aria-hidden="true">
          <rect x="2" y="2" width="12" height="12" rx="1.5" fill="var(--orange)"/>
        </svg>
        Friendlink (details TBA)
      </li>
    </ul>
  </section>

  <section class="card card--back">
    <div class="back-brand">
      <span class="back-brand__dot"></span>
      <span class="back-brand__name">wadol care</span>
    </div>
  </section>
</div>
</body>
</html>
```